Operator Qualification Testing Flyer

I have a 8x10 basic flyer that I created usin InDesign for one of our services our company provides. I would like to see more options for the layout and general design of the flyer. This flyer will be used as a template for the other services we provide. I will include the InDesign Folder with all the logos and images. Please feel free to use any logo design within the folder and you can change the font and/or colors as needed. I would like the final output in a Indesign package folder to be used in InDesign 2021

Target Market(s)

Business to Business marketing in the Oil and Gas industry

Font styles to use
Sans Serif

Colors
85cae6
85acd3
3377b5
0355a3
0792cd
ffffff
cedeed

Requirements
Must have
• I included/attached a couple of brochures styles that I do like.

```html
<!DOCTYPE html>
<html lang="en">
<head>
<meta charset="utf-8">
<title>Pipeline OQ Testing Flyer</title>
<link rel="stylesheet" href="https://fonts.googleapis.com/css2?family=Oswald:wght@500;600&family=Open+Sans:wght@400;600&family=Roboto:wght@300;400&display=swap">
<style>
:root{
  --ink:#1f1f22;
  --teal:#1d6b86;
  --teal-dark:#1a5d72;
  --stripe:#2ea7d8;
  --stripe-light:#5cc5ea;
  --band:#c8ecf7;
  --body:#333;
  --page:#e4e4e4;
  --white:#ffffff;
}
*{margin:0;padding:0;box-sizing:border-box}
html,body{width:1200px;height:2400px;overflow:hidden;background:var(--page)}
.flyer{position:absolute;left:0;top:450px;width:920px;height:1150px;background:var(--white);transform:scale(1.3043);transform-origin:0 0;overflow:hidden;font-family:"Open Sans",sans-serif;color:var(--body)}
.layer{position:absolute;left:0;top:0}
.brand{position:absolute;left:48px;top:70px;display:flex;align-items:center;gap:14px}
.brand-dot{width:62px;height:62px;border-radius:50%;background:var(--teal)}
.brand-name{font-family:"Open Sans",sans-serif;font-weight:600;font-size:28px;line-height:1.15;color:var(--ink)}
.headline{position:absolute;left:498px;top:165px;font-family:"Oswald",sans-serif;font-weight:600;font-size:124px;line-height:1;letter-spacing:-4px;color:var(--ink);transform:scaleX(.86);transform-origin:0 0}
.subline{position:absolute;left:534px;top:288px;font-family:"Oswald",sans-serif;font-weight:500;font-size:76px;line-height:1;letter-spacing:-2px;color:var(--teal);transform:scaleX(.82);transform-origin:0 0}
.pill{position:absolute;left:584px;top:683px;width:274px;height:36px;border-radius:12px;background:var(--teal-dark);color:var(--white);font-family:"Roboto",sans-serif;font-size:24px;line-height:36px;text-align:center}
.provide{position:absolute;left:538px;top:740px;width:342px}
.provide p{border-left:2px solid var(--ink);padding-left:16px;font-size:12.6px;line-height:1.38;text-align:justify;margin-bottom:20px}
.provide p:first-child{border-color:var(--teal)}
.section-head{position:absolute;left:47px;display:flex;align-items:center;gap:12px;font-family:"Roboto",sans-serif;font-size:24px;color:var(--ink)}
.section-head .accent{color:var(--teal);font-weight:300}
.icon{width:66px;height:66px;border-radius:50%;background:var(--ink);flex:none}
.icon.teal{background:var(--teal)}
.qual-head{top:732px}
.task-head{top:955px}
.para{position:absolute;left:61px;width:418px;font-size:12.8px;line-height:1.36;text-align:justify}
.qual-text{top:810px}
.task-text{top:1022px}
.contact{position:absolute;left:520px;display:flex;align-items:center;gap:12px;font-size:13px}
.contact .icon{width:40px;height:40px;display:flex;align-items:center;justify-content:center}
.call{top:990px}
.call strong{font-weight:400;font-size:21px;color:var(--teal);margin-left:4px}
.mail{top:1039px;letter-spacing:4px;font-size:13.5px}
.footer{position:absolute;left:0;top:1105px;width:920px;height:32px;background:var(--band);font-size:13px;letter-spacing:4px;text-align:center;line-height:32px;color:var(--ink)}
</style>
</head>
<body>
<article class="flyer">
  <svg class="layer backdrop" width="920" height="1150" role="img" aria-label="Photo of a pipeline worker in hard hat and coveralls tightening a valve on an oil field pipeline, fading into a light view of pipeline structures">
    <defs>
      <linearGradient id="photoTone" x1="0" y1="0" x2="1" y2="0">
        <stop offset="0" stop-color="#7d8fb3"/>
        <stop offset=".35" stop-color="#5f6f9f"/>
        <stop offset=".6" stop-color="#b4c8dc"/>
        <stop offset="1" stop-color="#eef3f8"/>
      </linearGradient>
      <linearGradient id="photoFade" x1="0" y1="0" x2="0" y2="1">
        <stop offset="0" stop-color="#ffffff" stop-opacity="0"/>
        <stop offset=".7" stop-color="#ffffff" stop-opacity="0"/>
        <stop offset="1" stop-color="#ffffff" stop-opacity=".85"/>
      </linearGradient>
    </defs>
    <polygon points="0,305 740,0 920,0 920,455 0,845" fill="url(#photoTone)"/>
    <polygon points="0,305 740,0 920,0 920,455 0,845" fill="url(#photoFade)"/>
  </svg>
  <svg class="layer stripes" width="920" height="1150" aria-hidden="true">
    <polygon points="0,752 460,612 460,626 0,766" fill="var(--stripe)"/>
    <polygon points="460,612 620,563 620,577 460,626" fill="var(--ink)"/>
    <polygon points="620,563 920,455 920,469 620,577" fill="var(--stripe-light)"/>
  </svg>
  <svg class="layer sign" width="920" height="1150" role="img" aria-label="Round yellow petroleum pipeline warning sign">
    <circle cx="712" cy="545" r="105" fill="#f5b417"/>
    <circle cx="712" cy="545" r="86" fill="#1d1d1d"/>
  </svg>

  <div class="brand">
    <span class="brand-dot"></span>
    <span class="brand-name">Meridian Field<br>Services Inc.</span>
  </div>

  <h1 class="headline">PIPELINE</h1>
  <h2 class="subline">OQ TESTING</h2>

  <div class="pill">WHAT WE PROVIDE</div>
  <div class="provide">
    <p>Meridian Field Services Inc. utilizes TradeCert pipeline program to administer OQ assessment testing on 127 covered tasks</p>
    <p>Upon completion of OQ testing the information is first transferred to TradeCert's Registry System and automatically uploaded to SafeLink.</p>
    <p>In addition to the benefits provided by SafeLink's database, the TradeCert Registry System houses all the completion information allowing candidates to share their training information and employers to verify successful covered task and level completions</p>
  </div>

  <h3 class="section-head qual-head"><span class="icon"></span><span><span class="accent">What Is Operator</span> Qualification?</span></h3>
  <p class="para qual-text">Operator Qualifications (OQ) for DOT Oil/Gas Pipelines are requirements set by Department of Transportation (DOT) and Pipeline and Hazardous Materials Safety Administration (PHMSA). To assure safety in the transport of hazardous gases and liquids in the nation's pipelines, pipeline operators who perform covered tasks must be qualified. Qualified means that an individual has been evaluated and can perform assigned covered tasks and recognize and react to abnormal operating conditions</p>

  <h3 class="section-head task-head"><span class="icon teal"></span><span><span class="accent">What Are</span> Covered Tasks?</span></h3>
  <p class="para task-text">Covered tasks are defined in an operator's written plan which defines specific job functions or activities personnel are qualified to perform on a pipeline facility.</p>

  <div class="contact call">
    <span class="icon"><svg width="18" height="18" viewBox="0 0 24 24" aria-hidden="true"><path d="M6.6 10.8a15 15 0 0 0 6.6 6.6l2.2-2.2a1 1 0 0 1 1-.25 11 11 0 0 0 3.6.6 1 1 0 0 1 1 1V20a1 1 0 0 1-1 1A17 17 0 0 1 3 4a1 1 0 0 1 1-1h3.5a1 1 0 0 1 1 1 11 11 0 0 0 .6 3.6 1 1 0 0 1-.25 1z" fill="#fff"/></svg></span>
    <span>call for more information <strong>555-014-2280</strong></span>
  </div>
  <div class="contact mail">
    <span class="icon teal"><svg width="18" height="18" viewBox="0 0 24 24" aria-hidden="true"><rect x="3" y="5" width="18" height="14" rx="2" fill="none" stroke="#fff" stroke-width="2"/><path d="M3 7l9 6 9-6" fill="none" stroke="#fff" stroke-width="2"/></svg></span>
    <span>info@meridianfield.co</span>
  </div>

  <footer class="footer">www.yourwebsite.com</footer>
</article>
</body>
</html>
```